4 Business Card templates for printing site

I want 4 business card templates (including a front and a back). You should provide a variety of designs covering a cross section of industries. It is fine if this is taken from variations on designs of previous work that you have produced.

**All the designs can be provided in one file**

The templates will be used for a website I am building which is targeted at servicing printing requirements for micro businesses (small business with less than 10 people). The first product to be launched is business cards. I will require ~500 designs so this initial phase is partly to identify potential designers with the capability to produce a broad range of designs to populate the site.

For this project 4 templates are required in total.
I want 2 generic designs - designs that are not industry specific (just simple classic modern templates), one that would have room for a logo to be added and one that works well as a design without a logo.

The other 4 designs can be across any industry. These will be for business without logos that still want to have a flavour of what they do represented by the card. These can include illustrations or photos.

Below is a list of industries which the templates will cover: Accountancy, Finance,Advertising, PR, Animal & Pet Care, Architecture, Builders, Childcare, cleaning, Driving Instructors, Education & Training, Electrician,Fashion, Florist / gardening,Hairdresser, Legal, Medical & Dental, Music & DJ, Painter, photographer, Plumber, Real Estate & Property, Salons, Spas, Wellbeing & Beauty, Sports & Fitness, Trademen - carpenter, handyman, Wedding Event & Party Planing.

For inspiration below are some sites where examples of templates can be seen:

Graphic / illustrative templates:
http://uk.plindrow.com/design-templates/business-cards/
and example of industry specific such as a plumber:
http://uk.plindrow.com/design-templates/business-cards/?search=industry:%22DIY%20%26%20Tradesmen%22&advsearch=1&filters=1

Example of card design treatment with photo front and back
http://www.zorvani.com/product/518273/details.htm

and of course the biggest online printer (although design quality is not very high).
http://www.quelbarn.co.uk/gallery/QBXAAAACAAAAAAA=/premium-business-cards.aspx?xnav=HowToDesign

For designers that submit work that does not win, I will pay £20 for specific templates that I want to use on the site.

For the winning designs I will require SVG files.

Target Market(s)

Micro businesses (small business with less than 10 people). Often self employed people.

Industry/Entity Type

Printing

Requirements
Nice to have
• I want to see well balanced designs, which have good use of space, font, colour and graphics.
Should not have
• I do not want to see poor quality "clip art" style designs!

```html
<!DOCTYPE html>
<html lang="en">
<head>
<meta charset="utf-8">
<title>Business card template – front and back</title>
<link href="https://fonts.googleapis.com/css2?family=Source+Sans+3:wght@400&display=swap" rel="stylesheet">
<style>
  :root {
    --backdrop: #ecebe8;
    --card: #ffffff;
    --card-edge: #dcdcdc;
    --ink: #4a4f57;
    --ink-soft: #8f949b;
    --pink: #e08ab8;
    --pink-light: #eeb3d2;
    --contact: #555a61;
  }
  * { box-sizing: border-box; margin: 0; padding: 0; }
  html, body {
    width: 1200px;
    height: 938px;
    overflow: hidden;
    background: var(--backdrop);
    font-family: "Source Sans 3", Arial, sans-serif;
    font-weight: 400;
  }
  .canvas { position: relative; width: 1200px; height: 938px; }

  .card {
    position: absolute;
    background: var(--card);
    border: 1px solid var(--card-edge);
    border-radius: 10px;
    box-shadow: 0 3px 10px rgba(0,0,0,0.12);
    overflow: hidden;
  }

  /* Front */
  .card-front { left: 52px; top: 50px; width: 707px; height: 488px; }
  .card-front .business-name {
    position: absolute;
    left: 0; right: 0; top: 196px;
    text-align: center;
    font-size: 100px;
    line-height: 1;
    letter-spacing: 4px;
    color: var(--ink);
  }

  /* Back */
  .card-back { left: 469px; top: 431px; width: 647px; height: 422px; }
  .card-back .accent-tab {
    position: absolute;
    right: 26px; top: 0;
    width: 80px; height: 120px;
    background: linear-gradient(to bottom, var(--pink-light) 0 50%, var(--pink) 50% 100%);
  }
  .card-back .business-name {
    position: absolute;
    right: 122px; top: 66px;
    font-size: 44px;
    line-height: 1;
    letter-spacing: 2px;
    color: var(--ink);
  }
  .card-back .person {
    position: absolute;
    left: 0; right: 0; top: 184px;
    text-align: center;
  }
  .card-back .person-name {
    font-size: 40px;
    line-height: 1.1;
    color: var(--pink);
  }
  .card-back .person-name .muted { color: var(--ink-soft); }
  .card-back .contact-list {
    list-style: none;
    margin-top: 8px;
    font-size: 24px;
    line-height: 26px;
    color: var(--contact);
  }
</style>
</head>
<body>
<main class="canvas">
  <section class="card card-front" aria-label="Card front">
    <p class="business-name">Larkwell</p>
  </section>

  <section class="card card-back" aria-label="Card back">
    <div class="accent-tab"></div>
    <p class="business-name">Larkwell</p>
    <div class="person">
      <p class="person-name">Your Name <span class="muted">Here</span></p>
      <ul class="contact-list">
        <li>000-000-000</li>
        <li>Address Line 1</li>
        <li>Address Line 2</li>
        <li>name@email.com</li>
      </ul>
    </div>
  </section>
</main>
</body>
</html>
```